Business Card Design

I am a Building Surveyor and run my own Building Consultat company, providing professional advice and services to builders, architects, designers, owners, etc.

Industry/Entity Type

Business

Contact Information for Business Card

Dorwen Halket BBldgSurv (Hons)
Managing Director

57 Quillon Rise, Marrick Heights WA 6148
Mobile 0438 271 594
Email Dorwen.halket@tarnwellpq.com

Requirements
Must have
• I would like the back of the business card to be one colour (a shade of either black or maroon, matching the colours of my logo). Positioned in the centre on the back of the business card is to be my logo.

The front of the card is to be white, with my contact information in either black or maroon. The ADBldgSurv after my name should be in a smaller font size than my name. I would also like a small logo somewhere on this side of the card.

```html
<!DOCTYPE html>
<html lang="en">
<head>
<meta charset="utf-8">
<title>Tarnwell – Business Card</title>
<link href="https://fonts.googleapis.com/css2?family=Didact+Gothic&family=Questrial&display=swap" rel="stylesheet">
<style>
  :root {
    --backdrop: #2b2b2b;
    --card-white: #ffffff;
    --card-charcoal: #5f5f5c;
    --maroon: #6e1f24;
    --band-grey: #5c5c5c;
    --text-grey: #4a4a4a;
    --text-soft: #6a6a6a;
    --logo-white: #f4f4f4;
  }
  * { margin: 0; padding: 0; box-sizing: border-box; }
  html, body { width: 1200px; height: 900px; overflow: hidden; }
  body {
    background: var(--backdrop);
    font-family: "Didact Gothic", "Questrial", sans-serif;
    position: relative;
  }
  .card {
    position: absolute;
    top: 297px;
    width: 500px;
    height: 306px;
    box-shadow: 0 10px 28px rgba(0,0,0,0.45);
    overflow: hidden;
  }
  .card-front { left: 70px; background: var(--card-white); }
  .card-back  { left: 630px; background: var(--card-charcoal); }

  .holder { position: absolute; left: 34px; top: 30px; }
  .holder-name {
    color: var(--maroon);
    font-size: 25px;
    font-weight: 700;
    letter-spacing: 1.5px;
    text-transform: uppercase;
    line-height: 1;
  }
  .holder-title, .address-line {
    color: var(--text-soft);
    font-size: 13px;
    line-height: 1.25;
  }
  .holder-title { margin-top: 4px; }
  .address-city {
    color: var(--text-grey);
    font-size: 13px;
    font-weight: 700;
    margin-top: 8px;
  }
  .contact-list { list-style: none; margin-top: 10px; }
  .contact-item {
    display: flex;
    align-items: center;
    gap: 8px;
    color: var(--text-grey);
    font-size: 14px;
    line-height: 1.45;
  }
  .contact-icon { width: 12px; height: 12px; flex: none; }

  .accent-band { position: absolute; left: 0; right: 0; top: 238px; height: 18px; display: flex; }
  .accent-band-grey { flex: 0 0 58%; background: var(--band-grey); }
  .accent-band-maroon { flex: 1; background: var(--maroon); }

  .brand-small {
    position: absolute;
    right: 30px;
    top: 180px;
    display: flex;
    align-items: center;
    gap: 6px;
    color: var(--maroon);
    font-family: "Questrial", sans-serif;
    font-size: 15px;
    letter-spacing: 1.5px;
    text-transform: uppercase;
  }
  .brand-dot { width: 14px; height: 14px; border-radius: 50%; background: var(--maroon); }

  .brand-large {
    position: absolute;
    inset: 0;
    display: flex;
    align-items: center;
    justify-content: center;
    gap: 16px;
    color: var(--logo-white);
    font-family: "Questrial", sans-serif;
    font-size: 40px;
    letter-spacing: 4px;
    text-transform: uppercase;
  }
  .brand-ring { width: 48px; height: 48px; border-radius: 50%; border: 3px solid var(--logo-white); }
</style>
</head>
<body>
  <section class="card card-front" aria-label="Business card front">
    <div class="holder">
      <h1 class="holder-name">Dorwen Halket</h1>
      <p class="holder-title">ADBldgSurv Director</p>
      <p class="address-line">57 Quillon Rise</p>
      <p class="address-city">Marrick Heights WA 6148</p>
      <ul class="contact-list">
        <li class="contact-item">
          <svg class="contact-icon" viewBox="0 0 12 12" aria-hidden="true">
            <rect x="2" y="0.5" width="8" height="11" rx="1.5" fill="var(--maroon)"/>
            <rect x="3.5" y="2" width="5" height="6" fill="#fff"/>
            <circle cx="6" cy="9.8" r="0.8" fill="#fff"/>
          </svg>
          0438 271 594
        </li>
        <li class="contact-item">
          <svg class="contact-icon" viewBox="0 0 12 12" aria-hidden="true">
            <rect x="0.5" y="2.5" width="11" height="7.5" fill="none" stroke="var(--maroon)" stroke-width="1"/>
            <polyline points="0.5,2.5 6,7 11.5,2.5" fill="none" stroke="var(--maroon)" stroke-width="1"/>
          </svg>
          Dorwen.halket@tarnwellpq.com
        </li>
      </ul>
    </div>
    <div class="brand-small"><span class="brand-dot"></span>Tarnwell</div>
    <div class="accent-band">
      <span class="accent-band-grey"></span>
      <span class="accent-band-maroon"></span>
    </div>
  </section>

  <section class="card card-back" aria-label="Business card back">
    <div class="brand-large"><span class="brand-ring"></span>Tarnwell</div>
  </section>
</body>
</html>
```